Business Report Cover

We need a revamped quarterly report cover to send to our clients. We asset manage commercial and residential properties throughout the the United States. We use a .pdf version of a cover that we've used for years but would like a fresh updated look for 2018. The cover should include our company logo (KVL Holdings) and a photo of the property as well as the Quarter/Year of the report.

Industry/Entity Type

Business

```html
<!DOCTYPE html>
<html lang="en">
<head>
<meta charset="utf-8">
<title>KVL Holdings — Quarterly Operating Report, 1st Quarter 2018</title>
<link rel="stylesheet" href="https://fonts.googleapis.com/css2?family=Arimo:wght@400;700&display=swap">
<style>
  :root {
    --brand-green: #0b7a3e;
    --ink: #111111;
    --paper: #ffffff;
  }
  * { margin: 0; padding: 0; box-sizing: border-box; }
  html, body {
    width: 927px;
    height: 1200px;
    overflow: hidden;
    background: var(--paper);
  }
  .cover {
    position: relative;
    width: 927px;
    height: 1200px;
    background: var(--paper);
    font-family: "Arimo", Arial, sans-serif;
    overflow: hidden;
  }
  .cover-art {
    position: absolute;
    inset: 0;
    width: 927px;
    height: 1200px;
  }
  .company-name {
    position: absolute;
    left: 56px;
    top: 96px;
    color: var(--ink);
    font-weight: 400;
    font-size: 62px;
    line-height: 1;
    white-space: nowrap;
  }
  .report-title {
    fill: var(--brand-green);
    font-family: "Arimo", Arial, sans-serif;
    font-weight: 700;
    font-size: 80px;
  }
  .report-year {
    position: absolute;
    right: 33px;
    bottom: 8px;
    color: var(--paper);
    font-weight: 700;
    font-size: 165px;
    line-height: 1;
    letter-spacing: -6px;
  }
  .report-quarter {
    position: absolute;
    left: 0;
    bottom: 0;
    width: 267px;
    height: 82px;
    background: var(--brand-green);
    color: var(--paper);
    font-weight: 400;
    font-size: 40px;
    display: flex;
    align-items: center;
    padding-left: 52px;
    white-space: nowrap;
  }
  .report-quarter sup {
    font-size: 22px;
    margin-right: 10px;
    line-height: 0;
    position: relative;
    top: -4px;
  }
</style>
</head>
<body>
<main class="cover">
  <svg class="cover-art" viewBox="0 0 927 1200" xmlns="http://www.w3.org/2000/svg">
    <defs>
      <linearGradient id="property-tones" x1="0" y1="0" x2="0" y2="1">
        <stop offset="0" stop-color="#f2f2f2"/>
        <stop offset="0.45" stop-color="#c9c9c9"/>
        <stop offset="0.62" stop-color="#6f6f6f"/>
        <stop offset="0.8" stop-color="#4a4a4a"/>
        <stop offset="1" stop-color="#2e2e2e"/>
      </linearGradient>
    </defs>
    <polygon class="property-photo" role="img"
      aria-label="Black and white photograph of a managed convenience store property with fuel canopy and pumps"
      points="0,1031 927,158 927,1200 0,1200" fill="url(#property-tones)"/>
    <polygon class="diagonal-band" points="0,1010 927,137 927,153 0,1026" fill="var(--brand-green)"/>
    <polygon class="diagonal-rule" points="0,1026 927,153 927,158 0,1031" fill="var(--ink)"/>
    <text class="report-title" x="28" y="966" textLength="1130" lengthAdjust="spacingAndGlyphs"
      transform="rotate(-43.3 28 966)">QUARTERLY OPERATING REPORT</text>
  </svg>

  <header class="company-name">KVL Holdings</header>

  <div class="report-year">2018</div>
  <div class="report-quarter">1<sup>st</sup>Quarter</div>
</main>
</body>
</html>
```